Full service residential and commercial painting
Finest quality attention to detail
All workmanship guaranteed
Email :brunomdufay@postvale.fr
Mobile: 0417386250
Industry/Entity Type
Residential
Contact Information for Business Card
Marten Dufay painting & decorating
Requirements
Nice to have
- Am thinking about someone can be painting my name on the card with MD painting with the logos of brush,pot tray and roller sleeves

```html
<!DOCTYPE html>
<html lang="en">
<head>
<meta charset="utf-8">
<title>Marten Dufay Painting &amp; Decorating – Business Card</title>
<link href="https://fonts.googleapis.com/css2?family=Bebas+Neue&family=Kaushan+Script&family=Open+Sans:wght@400;700&display=swap" rel="stylesheet">
<style>
  :root {
    --backdrop: #c9c9c9;
    --card: #f7f7f7;
    --orange: #f28c1c;
    --orange-deep: #ea6f14;
    --purple: #6d4a9c;
    --green: #5cb82e;
    --white: #ffffff;
  }
  * { margin: 0; padding: 0; box-sizing: border-box; }
  html, body { width: 1200px; height: 861px; overflow: hidden; }
  body {
    background: var(--backdrop);
    display: flex; align-items: center; justify-content: center;
    font-family: "Open Sans", sans-serif;
  }
  .card {
    position: relative;
    width: 980px; height: 560px;
    background: var(--card);
    box-shadow: 0 10px 30px rgba(0,0,0,.18);
    overflow: hidden;
  }
  .paint-band {
    position: absolute; left: 0; top: 0;
    width: 600px; height: 250px;
    background: linear-gradient(90deg, var(--orange-deep), var(--orange));
  }
  .roller-art {
    position: absolute; left: 600px; top: 20px;
    width: 340px; height: 260px;
    background: linear-gradient(135deg, #f6a33a, #f4b25a 60%, #cfcfcf);
    border-radius: 8px;
  }
  .buckets-art {
    position: absolute; left: 710px; top: 310px;
    width: 230px; height: 220px;
    background: linear-gradient(160deg, #e6e6e6, #bdbdbd 55%, #7dbf55);
    border-radius: 8px;
  }
  .brand {
    position: absolute; left: 56px; top: 26px;
    color: var(--white);
  }
  .brand-name {
    font-family: "Bebas Neue", sans-serif;
    font-size: 92px; line-height: .9; letter-spacing: 2px;
  }
  .brand-trade {
    font-family: "Kaushan Script", cursive;
    font-size: 38px; line-height: 1.1; margin-left: 40px;
  }
  .services {
    list-style: none; margin-top: 12px;
    font-size: 17px; line-height: 1.35;
  }
  .services li::before { content: "• "; }
  .contact {
    position: absolute; left: 40px; top: 290px;
    width: 650px;
    display: flex; flex-direction: column; gap: 22px;
  }
  .contact-row { display: flex; align-items: center; gap: 14px; }
  .contact-icon {
    width: 58px; height: 58px; border-radius: 50%;
    display: flex; align-items: center; justify-content: center;
    flex-shrink: 0;
  }
  .contact-icon svg { width: 30px; height: 30px; }
  .contact-row.email .contact-icon { background: var(--purple); }
  .contact-row.phone .contact-icon { background: var(--green); }
  .contact-text { font-weight: 700; font-size: 38px; letter-spacing: .3px; white-space: nowrap; }
  .contact-row.email .contact-text { color: var(--purple); }
  .contact-row.phone .contact-text { color: var(--green); }
</style>
</head>
<body>
  <div class="card">
    <div class="paint-band" role="img" aria-label="Orange rolled paint stripe"></div>
    <div class="roller-art" role="img" aria-label="Orange paint roller with silver handle"></div>
    <div class="buckets-art" role="img" aria-label="Two paint buckets, purple and green paint"></div>

    <div class="brand">
      <div class="brand-name">MARTEN DUFAY</div>
      <div class="brand-trade">Painting &amp; Decorating</div>
      <ul class="services">
        <li>Full service residential and commercial painting</li>
        <li>Finest quality attention to detail</li>
        <li>All workmanship guaranteed</li>
      </ul>
    </div>

    <div class="contact">
      <div class="contact-row email">
        <span class="contact-icon">
          <svg viewBox="0 0 24 24" fill="none" stroke="#fff" stroke-width="2"><rect x="2" y="5" width="20" height="14" rx="1"/><path d="M2 6l10 7 10-7"/></svg>
        </span>
        <span class="contact-text">brunomdufay@postvale.fr</span>
      </div>
      <div class="contact-row phone">
        <span class="contact-icon">
          <svg viewBox="0 0 24 24" fill="#fff"><path d="M6.6 10.8a15 15 0 006.6 6.6l2.2-2.2a1 1 0 011-.25 11.4 11.4 0 003.6.6 1 1 0 011 1V20a1 1 0 01-1 1A17 17 0 013 4a1 1 0 011-1h3.5a1 1 0 011 1c0 1.25.2 2.450.6 3.6a1 1 0 01-.25 1z"/></svg>
        </span>
        <span class="contact-text">0417386250</span>
      </div>
    </div>
  </div>
</body>
</html>
```